Fairway Outback Tee Saver Pass

We need a design for a plastic rewards card that we would like to offer to our customers. The rewards card is for customers to show other golf courses to indicate that they get a discount at that participating course. Our Company name is "Fairway Outback" the card is called the "Tee Saver Pass" and our tag line is "Swing Often Spend Little". We would like the card to have an Australian feel and and use the colours Black and Yellow.

Target Market(s)

Golfers

Industry/Entity Type

Plastic

Requirements
Must have
• We have attached how our previous version looked with the detail that needs to be on the card. However the addresses on the front of the card needs to be removed and replaced with www.fairwayoutback-example.com.au. On the back of the card the address needs to be changed to "Fairway Outback" P.O Box 4183, Coral Inlet W.A. Email: info@fairwayoutback-example.com.au

```html
<!DOCTYPE html>
<html lang="en">
<head>
<meta charset="utf-8">
<title>Fairway Outback – Tee Saver Pass</title>
<link rel="stylesheet" href="https://fonts.googleapis.com/css2?family=Noto+Sans:wght@400;700&family=Saira+Semi+Condensed:wght@400;600;700&display=swap">
<style>
  :root {
    --stage: #e9e6e0;
    --card: #231f20;
    --yellow: #ffe500;
    --white: #ffffff;
    --grey: #c9c9c9;
    --field: #ececec;
    --orange: #f0902a;
    --ball-light: #bdbdbd;
    --ball-dark: #2a2a2a;
    --display: "Saira Semi Condensed", sans-serif;
    --body: "Noto Sans", sans-serif;
  }
  * { margin: 0; padding: 0; box-sizing: border-box; }
  html, body { width: 1200px; height: 509px; overflow: hidden; }
  body { background: var(--stage); position: relative; }

  .card {
    position: absolute;
    width: 539px;
    height: 338px;
    background: var(--card);
    overflow: hidden;
    color: var(--white);
  }
  .card--front { left: 45px; top: 73px; }
  .card--back { left: 612px; top: 83px; }

  /* Front */
  .hero-ball {
    position: absolute;
    left: 13px; top: -5px;
    width: 224px; height: 224px;
    border-radius: 50%;
    background: radial-gradient(circle at 38% 30%, var(--ball-light) 0%, #8a8a8a 35%, #4a4a4a 65%, var(--ball-dark) 100%);
  }
  .brand-mark {
    position: absolute;
    display: flex;
    align-items: center;
    gap: 8px;
    font-family: var(--display);
    font-weight: 600;
    color: var(--white);
    white-space: nowrap;
  }
  .brand-mark__dot {
    width: 34px; height: 34px;
    border-radius: 50%;
    background: var(--orange);
    flex: none;
  }
  .card--front .brand-mark { right: 18px; top: 34px; font-size: 22px; }
  .front-title {
    position: absolute;
    left: 150px; width: 280px; top: 140px;
    text-align: center;
    font-family: var(--display);
    font-weight: 600;
    font-size: 28px;
    color: var(--yellow);
    letter-spacing: 0.5px;
  }
  .front-subtitle {
    position: absolute;
    left: 150px; width: 280px; top: 180px;
    text-align: center;
    font-family: var(--display);
    font-size: 17px;
    letter-spacing: 1px;
    color: var(--white);
  }
  .front-tagline {
    position: absolute;
    left: 0; right: 0; top: 250px;
    text-align: center;
    font-family: var(--display);
    font-weight: 700;
    font-size: 32px;
    color: var(--yellow);
    letter-spacing: 0.3px;
  }
  .front-url {
    position: absolute;
    left: 0; right: 0; top: 294px;
    text-align: center;
    font-family: var(--display);
    font-size: 16px;
    color: var(--grey);
    letter-spacing: 0.5px;
  }

  /* Back */
  .terms { position: absolute; left: 19px; top: 12px; right: 19px; font-family: var(--body); }
  .terms__heading { font-size: 14px; font-weight: 700; color: var(--yellow); line-height: 17px; }
  .terms__list { list-style: none; font-size: 13.5px; line-height: 15.5px; }
  .terms__list li { position: relative; padding-left: 19px; }
  .terms__list li::before {
    content: ""; position: absolute; left: 2px; top: 5px;
    width: 6px; height: 6px; border-radius: 50%; background: var(--yellow);
  }
  .field { position: absolute; top: 113px; font-family: var(--body); }
  .field__label { font-size: 13.5px; font-weight: 700; color: var(--yellow); height: 21px; }
  .field__box { height: 57px; background: var(--field); border: 1px solid #bdbdbd; }
  .field--name { left: 19px; width: 288px; }
  .field--expiry { left: 321px; width: 200px; }
  .contact-note {
    position: absolute; left: 19px; top: 216px;
    font-family: var(--body); font-size: 13.5px; line-height: 15px;
  }
  .address {
    position: absolute; left: 28px; top: 264px;
    font-family: var(--body); font-size: 13.5px; line-height: 16px;
  }
  .address__name { color: var(--yellow); font-weight: 700; }
  .card--back .brand-mark { right: 16px; top: 262px; font-size: 19px; gap: 7px; }
  .card--back .brand-mark__dot { width: 28px; height: 28px; }
</style>
</head>
<body>
  <section class="card card--front">
    <div class="hero-ball" role="img" aria-label="Large dimpled golf ball illustration"></div>
    <div class="brand-mark"><span class="brand-mark__dot"></span>Fairway Outback</div>
    <h1 class="front-title">Fairway Outback</h1>
    <p class="front-subtitle">Tee Saver Pass</p>
    <p class="front-tagline">SWING OFTEN SPEND LITTLE!</p>
    <p class="front-url">www.fairwayoutback-example.com.au</p>
  </section>

  <section class="card card--back">
    <div class="terms">
      <h2 class="terms__heading">Terms and Conditions</h2>
      <ul class="terms__list">
        <li>Cardholders must show their card to redeem offers at the participating outlets</li>
        <li>The Discounts apply to the card holder only.</li>
        <li>Golf course bookings are essential.</li>
        <li>The discounts available on the card are not valid with any other offer.</li>
      </ul>
    </div>
    <div class="field field--name">
      <div class="field__label">Card Holder Name</div>
      <div class="field__box"></div>
    </div>
    <div class="field field--expiry">
      <div class="field__label">Expiry date</div>
      <div class="field__box"></div>
    </div>
    <p class="contact-note">For information regarding this card contact:<br>The Administration Coordinator</p>
    <address class="address" style="font-style:normal">
      <span class="address__name">Fairway Outback</span><br>
      P.O Box 4183, Coral Inlet W.A.<br>
      Email: info@fairwayoutback-example.com.au
    </address>
    <div class="brand-mark"><span class="brand-mark__dot"></span>Fairway Outback</div>
  </section>
</body>
</html>
```